Redgate Business Card Design

We are a new small business specialising in under ground cable jointing and excavation works in NSW Australia.
Design I'm looking for is incorporating the Australian flag & excavator with out being to cheesy.
Maybe a faded washed out flag to help with overload of colour? & so its not the main focus.
Very open to creative out of the box designs!

Target Market(s)

Building & Construction

Industry/Entity Type

Construction

Contact Information for Business Card

Redgate Cable Jointing & Excavations
Colin Barwick

Ph: 0412 938 560
E: colin.barwick@tellnet.example

Reverse Side
Services we offer:
High Voltage & Low Voltage Cable Jointing
Polymeric & paperlead jointing & terminations
Trenching & Auger Drilling 150 - 600mm
Site preparation / leveling / clearing
Driveway / Footpath / Turf Prep
Rubbish Removal
Tree & Stump removal
Footings & Post holes
Drainage
Service Installs
Gravels & Sands available
Any general Earth moving needs
Reliable Free Quotes
Fully Insured

Font styles to use
Serif
Script

Requirements
Nice to have
• small excavator (See uploaded picture)

```html
<!DOCTYPE html>
<html lang="en">
<head>
<meta charset="utf-8">
<title>Redgate Business Card Design</title>
<link rel="stylesheet" href="https://fonts.googleapis.com/css2?family=Lobster&family=Libre+Baskerville:wght@400;700&display=swap">
<style>
  :root {
    --page: #ecebe8;
    --card: #ffffff;
    --aubergine: #24141f;
    --ink: #2a2228;
    --muted: #5a5458;
    --sky-light: #f2f2f2;
    --sky-mid: #c9c9c9;
    --machine: #e07a3c;
    --faint: #cfcbcf;
  }
  * { margin: 0; padding: 0; box-sizing: border-box; }
  html, body { width: 1200px; height: 892px; overflow: hidden; background: var(--page); }
  .canvas { position: relative; width: 1200px; height: 892px; }

  .card {
    position: absolute;
    background: var(--card);
    overflow: hidden;
    box-shadow: 0 6px 18px rgba(0,0,0,.18);
  }

  /* Front */
  .card-front { left: 80px; top: 136px; width: 360px; height: 620px; }
  .front-photo {
    position: absolute; inset: 0 0 220px 0;
    background:
      radial-gradient(ellipse 55% 45% at 60% 60%, rgba(224,122,60,.55), rgba(224,122,60,0) 70%),
      linear-gradient(180deg, var(--sky-light) 0%, var(--sky-mid) 100%);
  }
  .front-title {
    position: absolute; top: 34px; left: 20px; right: 20px;
    font-family: "Lobster", cursive;
    font-size: 30px; line-height: 1.15; text-align: center;
    color: var(--ink);
    text-shadow: 0 0 6px #fff, 0 0 2px #fff;
  }
  .front-band { position: absolute; left: 0; right: 0; bottom: 0; height: 300px; }
  .front-contact {
    position: absolute; left: 0; right: 0; bottom: 70px;
    text-align: center; color: #fff;
    font-family: "Libre Baskerville", serif;
  }
  .contact-name { font-size: 30px; font-weight: 700; margin-bottom: 22px; }
  .contact-line { font-size: 19px; line-height: 1.5; }

  /* Back */
  .card-back { left: 490px; top: 260px; width: 640px; height: 372px;
    background: linear-gradient(135deg, #ffffff 40%, #f1f0f1 100%); }
  .services-list {
    position: absolute; left: 40px; top: 34px;
    list-style: none;
    font-family: "Libre Baskerville", serif;
    font-size: 14.5px; line-height: 21.5px; color: var(--muted);
  }
  .services-list li { padding-left: 22px; position: relative; }
  .services-list li::before {
    content: ""; position: absolute; left: 2px; top: 7px;
    width: 7px; height: 7px; border: 1.5px solid var(--muted); border-radius: 50%;
  }
  .services-mark {
    position: absolute; right: 40px; top: 70px; width: 200px; height: 240px;
    background: radial-gradient(ellipse at 50% 55%, var(--faint), rgba(207,203,207,0) 70%);
  }
  .services-heading {
    position: absolute; right: 36px; bottom: 34px;
    font-family: "Lobster", cursive; font-size: 38px; color: var(--ink);
  }
</style>
</head>
<body>
<main class="canvas">

  <section class="card card-front">
    <div class="front-photo" role="img" aria-label="Photo of an orange mini excavator against a pale grey cloudy sky"></div>
    <h1 class="front-title">Redgate Cable Jointing<br>&amp;<br>Excavations</h1>
    <svg class="front-band" viewBox="0 0 360 300" preserveAspectRatio="none" aria-hidden="true">
      <path d="M0 40 C 80 10, 150 20, 210 60 S 320 70, 360 30 L360 300 L0 300 Z" fill="var(--aubergine)"/>
      <path d="M0 40 C 80 10, 150 20, 210 60 S 320 70, 360 30" fill="none" stroke="#ffffff" stroke-width="3"/>
    </svg>
    <div class="front-contact">
      <p class="contact-name">Colin Barwick</p>
      <p class="contact-line">0412 938 560</p>
      <p class="contact-line">colin.barwick@tellnet.example</p>
    </div>
  </section>

  <section class="card card-back">
    <ul class="services-list">
      <li>High Voltage &amp; Low Voltage Cable Jointing</li>
      <li>Polymeric &amp; paperlead jointing &amp; terminations</li>
      <li>Trenching &amp; Auger Drilling 150 - 600mm</li>
      <li>Site preparation / leveling / clearing</li>
      <li>Driveway / Footpath / Turf Prep</li>
      <li>Rubbish Removal</li>
      <li>Tree &amp; Stump removal</li>
      <li>Footings &amp; Post holes</li>
      <li>Drainage</li>
      <li>Service Installs</li>
      <li>Gravels &amp; Sands available</li>
      <li>Any general Earth moving needs</li>
      <li>Reliable Free Quotes</li>
      <li>Fully Insured</li>
    </ul>
    <div class="services-mark" role="img" aria-label="Faint grey kangaroo silhouette illustration"></div>
    <h2 class="services-heading">Services we offer:</h2>
  </section>

</main>
</body>
</html>
```